Dorsey K. Whitfield Business Card

We need a business card for our company Dorsey K. Whitfield Heating & Plumbing to be distributed to potential customers. It should follow the color scheme of our logo and have a modern upscale and masculine look.

The logo is attached and the info below should also be included:

5187 W. Quarry Bend Rd.
Elmhaven, PA 17582

Tobias R. Whitfield
(717) 593-8126
tobiasreedwhitfield@mailvane.com
dorseykwhitfield.com
PA #038419

Industry/Entity Type

Business

Contact Information for Business Card

5187 W. Quarry Bend Rd.
Elmhaven, PA 17582

Tobias R. Whitfield
(717) 593-8126
tobiasreedwhitfield@mailvane.com
dorseykwhitfield.com
PA #038419

Colors

Designer to choose colors to be used in the design.

Requirements
Must have
• Information above included

```html
<!DOCTYPE html>
<html lang="en">
<head>
<meta charset="utf-8">
<title>Dorsey K. Whitfield Heating &amp; Plumbing – Business Card</title>
<link rel="stylesheet" href="https://fonts.googleapis.com/css2?family=Roboto:wght@400;500&family=Roboto+Condensed:wght@700&display=swap">
<style>
  :root {
    --backdrop: #2b2b2b;
    --brand-blue: #0654a3;
    --brand-green: #a9cf38;
    --card-white: #f1f1f1;
    --text-light: #ffffff;
  }
  * { box-sizing: border-box; margin: 0; padding: 0; }
  html, body {
    width: 1200px; height: 960px; overflow: hidden;
    background: var(--backdrop);
    font-family: "Roboto", Arial, sans-serif;
  }
  .canvas { position: relative; width: 1200px; height: 960px; }

  .card { position: absolute; width: 600px; overflow: hidden; }

  /* Front face */
  .card-front {
    left: 322px; top: 108px; height: 342px;
    background: var(--brand-blue);
    color: var(--text-light);
  }
  .front-wordmark {
    position: absolute; left: 0; right: 0; top: 146px;
    text-align: center;
    font-family: "Roboto Condensed", Arial, sans-serif;
    font-weight: 700; font-size: 34px; letter-spacing: 1px;
    text-transform: uppercase;
  }
  .front-web {
    position: absolute; left: 0; right: 0; top: 292px;
    text-align: center; font-size: 14px; letter-spacing: 5.2px;
  }

  /* Back face */
  .card-back {
    left: 320px; top: 493px; height: 342px;
    background: var(--card-white);
  }
  .back-brand {
    position: absolute; left: 0; right: 0; top: 98px;
    display: flex; align-items: center; justify-content: center; gap: 12px;
    color: var(--brand-blue);
    font-family: "Roboto Condensed", Arial, sans-serif;
    font-weight: 700; font-size: 27px; text-transform: uppercase;
  }
  .back-brand .brand-square {
    width: 26px; height: 26px; background: var(--brand-blue);
  }
  .info-band {
    position: absolute; left: 0; top: 233px; width: 600px; height: 109px;
    display: flex; gap: 5px;
  }
  .info-person {
    width: 297px; background: var(--brand-blue); color: var(--text-light);
    text-align: right; padding: 17px 26px 0 0;
  }
  .person-name {
    font-family: "Roboto Condensed", Arial, sans-serif;
    font-weight: 700; font-size: 21px; text-transform: uppercase;
    margin-bottom: 6px;
  }
  .person-address { font-size: 14.5px; line-height: 19px; }
  .info-contact {
    flex: 1; background: var(--brand-green); color: var(--text-light);
    padding: 17px 0 0 26px; font-size: 14px; line-height: 19.3px;
  }
  .contact-line { display: flex; align-items: center; gap: 8px; white-space: nowrap; }
  .contact-line svg { width: 13px; height: 13px; flex: none; fill: var(--text-light); }
</style>
</head>
<body>
<div class="canvas">

  <section class="card card-front" aria-label="Card front">
    <div class="front-wordmark">Dorsey K. Whitfield</div>
    <div class="front-web">www.dorseykwhitfield.com</div>
  </section>

  <section class="card card-back" aria-label="Card back">
    <div class="back-brand">
      <span class="brand-square"></span>
      <span>Dorsey K. Whitfield</span>
    </div>
    <div class="info-band">
      <div class="info-person">
        <div class="person-name">Tobias R. Whitfield</div>
        <div class="person-address">5187 W. Quarry Bend Rd.<br>Elmhaven, PA 17582</div>
      </div>
      <div class="info-contact">
        <div class="contact-line">
          <svg viewBox="0 0 24 24" aria-hidden="true"><path d="M6.6 10.8a15.1 15.1 0 0 0 6.6 6.6l2.2-2.2a1 1 0 0 1 1-.25 11.4 11.4 0 0 0 3.6.57 1 1 0 0 1 1 1V20a1 1 0 0 1-1 1A17 17 0 0 1 3 4a1 1 0 0 1 1-1h3.5a1 1 0 0 1 1 1c0 1.25.2 2.45.57 3.57a1 1 0 0 1-.25 1z"/></svg>
          <span>(717) 593-8126</span>
        </div>
        <div class="contact-line">
          <svg viewBox="0 0 24 24" aria-hidden="true"><path d="M2 5h20v14H2zM3.5 6.5 12 13l8.5-6.5z" fill-rule="evenodd"/></svg>
          <span>tobiasreedwhitfield@mailvane.com</span>
        </div>
        <div class="contact-line">
          <svg viewBox="0 0 24 24" aria-hidden="true"><circle cx="12" cy="12" r="10"/></svg>
          <span>dorseykwhitfield.com</span>
        </div>
        <div class="contact-line"><span>PA #038419</span></div>
      </div>
    </div>
  </section>

</div>
</body>
</html>
```